Illustration Style Book Cover for Business Book

I have written a book called "The Corner Shop Keeper's Handbook". The title should be self-explanatory. It's a how-to for the owner or manager of a small business on a variety of subjects like makreting, operations, finance, managing people, etc.
I have no pre-defined notions about what i want this to look like and I would like the designer to take full creative license. The "owners manual" concept should come through in the design.

Target Market(s)

Small Business Owners and Operators

Industry/Entity Type

All - Small business

Font styles to use
Sans Serif

Colors

Designer to choose colors to be used in the design.

Requirements
Nice to have
• Should look like an “owners manual"
Should not have
• Photos

```html
<!DOCTYPE html>
<html lang="en">
<head>
<meta charset="utf-8">
<title>The Corner Shop Keeper's Handbook – Cover Spread</title>
<link href="https://fonts.googleapis.com/css2?family=Bebas+Neue&family=Oswald:wght@500&family=Montserrat:wght@400&display=swap" rel="stylesheet">
<style>
  :root {
    --page: #ffffff;
    --teal: #0fbab0;
    --teal-light: #4cc8bf;
    --teal-deep: #0aa99f;
    --navy: #1c2235;
    --navy-glow: #3a4a61;
    --ink: #232b3b;
    --white: #ffffff;
    --accent: #14b8ad;
  }
  * { margin: 0; padding: 0; box-sizing: border-box; }
  html, body {
    width: 720px; height: 1200px; overflow: hidden;
    background: var(--page);
  }
  .canvas { position: relative; width: 720px; height: 1200px; }

  .spread {
    position: absolute; left: 20px; top: 349px;
    width: 680px; height: 502px;
    background: radial-gradient(ellipse 60% 55% at 55% 55%, var(--teal-light), var(--teal) 70%, var(--teal-deep));
    overflow: hidden;
  }

  /* Back flap column */
  .back-panel {
    position: absolute; left: 0; top: 0; width: 162px; height: 502px;
    background: radial-gradient(ellipse 90% 60% at 60% 45%, var(--navy-glow), var(--navy) 80%);
  }
  .back-title { position: absolute; left: 24px; top: 24px; }
  .back-title span {
    display: block; font-family: "Bebas Neue", sans-serif; line-height: 0.82;
  }
  .back-title .t-the { font-size: 23px; color: var(--white); }
  .back-title .t-corner { font-size: 48px; color: var(--accent); }
  .back-title .t-shop { font-size: 42px; color: var(--accent); }
  .back-title .t-keeper { font-size: 33px; color: var(--white); }
  .back-title .t-handbook { font-size: 33px; color: var(--white); }

  .blurb {
    position: absolute; left: 25px; top: 190px; width: 112px;
    font-family: "Montserrat", sans-serif; font-size: 6.3px; line-height: 7.9px;
    color: var(--white); text-align: justify;
  }
  .blurb p + p { margin-top: 8px; }
  .website {
    position: absolute; left: 0; width: 162px; top: 466px; text-align: center;
    font-family: "Montserrat", sans-serif; font-size: 6px; letter-spacing: 0.35em;
    color: var(--accent);
  }

  /* Back cover */
  .photo-box {
    position: absolute; left: 198px; top: 29px; width: 92px; height: 99px;
    background: var(--white);
  }
  .back-author {
    position: absolute; left: 188px; top: 144px;
    font-family: "Oswald", sans-serif; font-size: 14px; letter-spacing: 0.2em;
    color: var(--white);
  }
  .bio {
    position: absolute; left: 188px; top: 166px; width: 113px;
    font-family: "Montserrat", sans-serif; font-size: 6.3px; line-height: 7.9px;
    color: var(--ink); text-align: justify;
  }
  .back-art {
    position: absolute; left: 196px; top: 274px; width: 86px; height: 114px;
    background: linear-gradient(160deg, rgba(255,255,255,0.25), rgba(10,140,132,0.35));
    border-radius: 4px;
  }
  .info-box {
    position: absolute; left: 188px; top: 410px; width: 118px; height: 72px;
    background: var(--white);
  }

  /* Spine */
  .spine-text {
    position: absolute; left: 330px; top: 29px; width: 20px; height: 445px;
    writing-mode: vertical-rl;
    font-family: "Bebas Neue", sans-serif; font-size: 19px; line-height: 20px;
    color: var(--white); letter-spacing: 0.02em; white-space: nowrap;
  }
  .spine-text .spine-gap { display: inline-block; height: 22px; }

  /* Front cover */
  .front-title { position: absolute; left: 383px; top: 24px; }
  .front-title span {
    display: block; font-family: "Bebas Neue", sans-serif; line-height: 0.84;
  }
  .front-title .t-the { font-size: 56px; color: var(--white); }
  .front-title .t-corner { font-size: 112px; color: var(--ink); }
  .front-title .t-shop { font-size: 96px; color: var(--ink); }
  .front-title .t-keeper { font-size: 74px; color: var(--white); }
  .front-title .t-handbook { font-size: 64px; color: var(--white); }

  .front-art {
    position: absolute; left: 566px; top: 300px; width: 114px; height: 202px;
    background: linear-gradient(165deg, rgba(255,255,255,0.22), rgba(10,140,132,0.4));
  }
  .front-author {
    position: absolute; left: 385px; top: 448px;
    font-family: "Oswald", sans-serif; font-size: 21px; letter-spacing: 0.22em;
    color: var(--white);
  }
</style>
</head>
<body>
<div class="canvas">
  <section class="spread">
    <div class="back-panel">
      <h2 class="back-title">
        <span class="t-the">The</span>
        <span class="t-corner">Corner</span>
        <span class="t-shop">Shop</span>
        <span class="t-keeper">Keeper’s</span>
        <span class="t-handbook">Handbook</span>
      </h2>
      <div class="blurb">
        <p>Lorem ipsum dolor sit amet, consectetur adipiscing elit. Curabitur in magna sit amet nulla aliquet vehicula. Morbi dictum, nunc et suscipit congue, leo orci vehicula felis, ac tristique ipsum turpis sed quam. Aenean luctus dolor id ex suscipit volutpat. Vivamus dapibus sagittis velit et euismod. Pellentesque ac sagittis velit, vel tempus mauris. Suspendisse ultricies pharetra malesuada. Aenean a vehicula ante.</p>
        <p>Cras tristique elit nibh, vitae molestie justo iaculis sed. Mauris non vestibulum dolor. Nunc cursus consequat libero, sit amet molestie magna facilisis placerat. Proin id facilisis nisl. Quisque eros mauris, consequat placerat imperdiet eget, hendrerit vel augue. Aliquam in enim et enim sagittis semper at at erat. Pellentesque est dui, blandit ullamcorper ullamcorper vitae, pulvinar quis odio. Nam feugiat, lorem ut varius lacinia, erat nisi tempus metus, vitae feugiat odio felis ac dui. Nulla facilisi. Sed ut neque nisi. In malesuada condimentum nisi quis ornare.</p>
      </div>
      <div class="website">www.website.com</div>
    </div>

    <div class="photo-box"></div>
    <div class="back-author">AUTHOR NAME</div>
    <p class="bio">Donec blandit accumsan nulla, nec vehicula velit varius in. Morbi luctus libero ut odio vulputate elementum. Cras facilisis libero orci, ac tempus enim cursus quis. Mauris porttitor erat eget sagittis lacinia. Vestibulum ut suscipit tortor. Cras nec feugiat mi, vitae rhoncus sem. Ut quis aliquet sem. Morbi tempor metus id ligula tempor pretium.</p>
    <div class="back-art" role="img" aria-label="Small illustration of a businessman placing a block on a rising stack of steps"></div>
    <div class="info-box"></div>

    <div class="spine-text">THE CORNER SHOP KEEPER’S HANDBOOK<span class="spine-gap"></span>AUTHOR NAME</div>

    <h1 class="front-title">
      <span class="t-the">The</span>
      <span class="t-corner">Corner</span>
      <span class="t-shop">Shop</span>
      <span class="t-keeper">Keeper’s</span>
      <span class="t-handbook">Handbook</span>
    </h1>
    <div class="front-art" role="img" aria-label="Illustration of a businessman in a suit stacking blocks into rising steps"></div>
    <div class="front-author">AUTHOR NAME</div>
  </section>
</div>
</body>
</html>
```